Cover for novel by Dorian T. Velkam

I need a book cover for a young adult novel about a group of teenagers fleeing the repressive government of their home country pursued by cruel government agents. They must cross a river to reach a neighboring country where they will be safe. My idea is for a minimalist design, perhaps with a birds-eye view of a rowboat sitting in blue water with the oars crossed. The boat could be an abstract charcoal or pen-and-ink sketch. Of course, I'm open to ideas. Will need the front, spine, and back cover for hardback and paperback editions. Plus, the cover for eBook and audiobook versions. The book's title is: VELVET QUARRY, the author name is Dorian T. Velkam.

```html
<!DOCTYPE html>
<html lang="en">
<head>
<meta charset="utf-8">
<title>Velvet Quarry — Dorian T. Velkam</title>
<link href="https://fonts.googleapis.com/css2?family=Bebas+Neue&family=Oswald:wght@300&display=swap" rel="stylesheet">
<style>
  :root {
    --backdrop: #d3d3d3;
    --mist: #f3f3f3;
    --haze: #d9dee4;
    --water-light: #aab5c4;
    --water-mid: #5a6b8c;
    --navy: #1f2b50;
    --navy-deep: #1a2446;
    --boat-dark: rgba(22, 30, 52, 0.92);
    --boat-mid: rgba(38, 50, 80, 0.55);
    --title-ink: #1e2a58;
    --band: #3f6089;
    --author-ink: #eef2f7;
  }
  * { margin: 0; padding: 0; box-sizing: border-box; }
  html, body {
    width: 1200px;
    height: 1000px;
    overflow: hidden;
    background: var(--backdrop);
  }
  .stage {
    width: 1200px;
    height: 1000px;
    display: flex;
    align-items: center;
    justify-content: center;
  }
  .book-cover {
    position: relative;
    width: 650px;
    height: 920px;
    overflow: hidden;
    background: var(--navy-deep);
  }
  .cover-photo {
    position: absolute;
    inset: 0;
    background: linear-gradient(
      to bottom,
      var(--mist) 0%,
      var(--haze) 22%,
      var(--haze) 32%,
      var(--water-light) 48%,
      var(--water-mid) 68%,
      var(--navy) 84%,
      var(--navy-deep) 100%
    );
  }
  .boat-photo {
    position: absolute;
    left: 0;
    top: 440px;
    width: 650px;
    height: 210px;
    background: radial-gradient(
      ellipse 48% 42% at 48% 52%,
      var(--boat-dark) 0%,
      var(--boat-dark) 45%,
      var(--boat-mid) 75%,
      rgba(38, 50, 80, 0) 100%
    );
  }
  .book-title {
    position: absolute;
    top: 172px;
    left: 0;
    right: 0;
    text-align: center;
    font-family: "Bebas Neue", "Oswald", sans-serif;
    font-weight: 400;
    font-size: 100px;
    line-height: 1;
    letter-spacing: 1px;
    color: var(--title-ink);
  }
  .author-band {
    position: absolute;
    top: 813px;
    left: 0;
    right: 0;
    height: 35px;
    background: var(--band);
  }
  .author-name {
    position: absolute;
    top: 801px;
    left: 0;
    right: 0;
    text-align: center;
    font-family: "Oswald", sans-serif;
    font-weight: 300;
    font-size: 41px;
    line-height: 56px;
    letter-spacing: 3px;
    color: var(--author-ink);
  }
</style>
</head>
<body>
  <main class="stage">
    <section class="book-cover">
      <div class="cover-photo" role="img" aria-label="Misty rain-speckled water fading from pale fog with a faint treeline down to deep navy"></div>
      <div class="boat-photo" role="img" aria-label="Photograph of a weathered wooden rowboat with an oar resting across it, floating on the dark water"></div>
      <h1 class="book-title">VELVET QUARRY</h1>
      <div class="author-band"></div>
      <p class="author-name">DORIAN T. VELKAM</p>
    </section>
  </main>
</body>
</html>
```